Create the BEST and COOLEST website for events and media company!

Hi there. I am a start-up events and conferences company with a twist, and we are seeking a highly modern website for our company Lumen Harbor Media. Our company believes that (like the social networking theory) that each and every one of us is connected to anyone on the planet in six connections or less. E.g. I know someone, who knows someone, who knows someone. Hence, the name Lumen Harbor Media.

I have included the copy for the website attached.

While we do have a business audience, they are in the fields of technology from the banking, health, government sector. We would like our website to be edgy, fresh and steer away from stuffy corporate images.

To give you an idea, our website menu tabs will be labelled:
HOME: This will include a corporate video that’s being created next week for me. However, please still design this page with a very striking background image that fills the whole page. You can run the copy and put a mock video for me to just see the layout (we can insert the finished video later).

ROCKSTARS: this will show pictures of highly powerful leaders speaking on stage; with a highly engaged audience watching. We want to show we have the world’s best technology International speakers “rockstars” who are the best in their game when it comes to talking about the future of technology.

LOCAL LEGENDS: like the international ‘rockstar’ speakers we would bring over to Australia to present; this LOCAL LEGENDS page should show we have the best home-grown Chief business people speaking at conferences and smaller powerful roundtable luncheons.

UNSUNG HEROES: this is more the people in the audience who ask questions on a microphone; those that attend the conferences; or a speaking to people at a conference.

THE BAND: this is like an ‘about us’ – just a funkier name to tie in with the theme of rockstars, etc.

THE PARTNERS: this is like a sponsor client page, where we invite people to partner with us and sponsor our events and conferences.

YOU & DORIAN FLECK: Dorian Fleck is a famous actor who made the term ‘six degrees of separation’ very popular. This page will have a little bit of an introduction, but mainly have the following video fill the landing page: https://www.vidstreamhub.example/watch?v=Qzt-plK4WB8

Website Functionality and Features:

• Try and make the ‘vibe’ and look and feel consistent, hip and modern (but still maintain a professional look). At the end of the day, people looking at our website are very senior business chiefs of organisations and also marketing chiefs.
• We may add more pages once we become established, so the website needs to ensure we can do that easily.
• We want pictures to not look stock photos. We want them to fresh, innovative, inspirational.
• Images should have a ‘wow’ factor. Like this one: https://www.stockframebank.example/detail/news-photo/general-view-of-crowd-during-brightloop-talks-2018-news-photo/481203967
• Need a mix of speaker, stage, audience, pictures. While we want to be fresh, edgy and contemporary we need to remember our viewers are the big chiefs of businesses – so lets try and have cool shots, but ensure there is a link to the business decision makers in a modern way. They all don’t have to wear suits, but not too casual either
• Other types of imagery I like is this one: https://www.stockframebank.example/detail/photo/smiling-audience-using-smart-phone-flashlights-for-royalty-free-image/372815094.
• The following are ok, not wow – but to give you an idea:
• https://www.stockframebank.example/detail/photo/smiling-male-speaker-in-wheelchair-on-stage-royalty-free-image/372816288
https://www.stockframebank.example/detail/photo/smiling-woman-with-camera-phone-in-dark-audience-royalty-free-image/372817452
https://www.stockframebank.example/detail/photo/audience-using-camera-phones-royalty-free-image/376630581
https://www.stockframebank.example/detail/photo/male-speaker-on-stage-talking-to-audience-royalty-free-image/372818736

NB: Logos are supplied in low resolution, but I can send you high resolution also
Updates

Hi there I will be adding two low-resolution images of my business partner and I for the ABOUT US page which is called THE BAND in the menu tab.

Hi everyone, thank you for your designs. I have uploaded a MAIN SCREEN IDEAS word document to give you further ideas of how the options I like for the main landing page on the home page. Hope this helps!

Target Market(s)

High end business people in marketing and business.

Coding

Coded - Design and coding required

Number of Pages Required

5+ page

Font styles to use
Sans Serif

Requirements
Must have
• Fresh, inspirational and aspirational designs. We need to make events and conferences look exciting and that we are bring the best technology speakers (like BrightLoop events) to our audience of marketing and technology professionals.
Should not have
• Cheesy, old stock photos; or pictures of American executives as this is for an Australian audience.
• PLEASE do not include an UPCOMING EVENTS or a SPEAKERS section as we will not be having this showcasing. You can feature ROCK STARS, LOCAL LEGENDS and UNSUNG HEROES if you like on the home page + the video of YOU and DORIAN FLECK (with his picture on the video box with a play button)

```html
<!DOCTYPE html>
<html lang="en">
<head>
<meta charset="utf-8">
<title>Lumen Harbor Media</title>
<link rel="stylesheet" href="https://fonts.googleapis.com/css2?family=Montserrat:wght@400;500;600&family=Open+Sans:wght@400;600&display=swap">
<style>
  :root{
    --ink:#1e1e1e;
    --body:#3a3a3a;
    --white:#ffffff;
    --stone-dark:#232323;
    --stone-mid:#3c3c3c;
    --stone-light:#4c4c4c;
    --muted:#cfcfcf;
    --shadow-block:#dcdcdc;
    --accent:#d8251d;
  }
  *{margin:0;padding:0;box-sizing:border-box}
  html,body{width:1200px;height:2683px;overflow:hidden;background:var(--white)}
  body{font-family:"Open Sans",Arial,sans-serif;color:var(--body);position:relative}
  .stone{
    background:
      radial-gradient(ellipse at 30% 20%,rgba(255,255,255,.07),transparent 60%),
      radial-gradient(ellipse at 80% 80%,rgba(0,0,0,.35),transparent 65%),
      linear-gradient(160deg,var(--stone-light),var(--stone-mid) 45%,var(--stone-dark));
  }
  section,header,footer{position:absolute;left:0;width:1200px}

  /* Brand lockup: circle above name */
  .brand{position:absolute;display:flex;flex-direction:column;align-items:center;gap:8px;color:var(--white);font-family:"Montserrat",Arial,sans-serif;font-weight:400;letter-spacing:.1em;text-transform:uppercase;white-space:nowrap}
  .brand-dot{display:block;width:34px;height:34px;border:2px solid var(--white);border-radius:50%}

  /* Hero */
  .hero{top:0;height:674px}
  .hero .brand{left:188px;top:14px;font-size:12px}
  .main-nav{position:absolute;left:400px;width:628px;top:72px;display:flex;justify-content:space-between;font-family:"Montserrat",Arial,sans-serif;font-size:11px;color:var(--white);text-transform:uppercase;white-space:nowrap}
  .hero-video{position:absolute;left:218px;top:156px;width:765px;height:452px;border:7px solid var(--white);
    background:radial-gradient(circle at 30% 35%,#b4523a,#5a2a22 45%,#2a1a18 90%)}
  .play{position:absolute;left:50%;top:50%;transform:translate(-50%,-50%)}

  /* Gigs */
  .gigs{top:674px;height:540px}
  .gigs-shadow{position:absolute;left:161px;top:154px;width:536px;height:302px;background:var(--shadow-block)}
  .gigs-photo{position:absolute;left:173px;top:89px;width:524px;height:360px;
    background:radial-gradient(circle at 70% 40%,#6a5a3a,#2a2a30 55%,#141418)}
  .section-title{font-family:"Montserrat",Arial,sans-serif;font-weight:400;color:var(--ink);text-transform:uppercase}
  .gigs .section-title{position:absolute;left:721px;top:92px;font-size:36px}
  .copy{font-size:10.8px;line-height:21px;color:var(--body)}
  .gigs .copy{position:absolute;left:721px;top:150px;width:310px}

  /* Features */
  .features{top:1214px;height:613px}
  .features h2{position:absolute;left:0;width:1200px;top:95px;text-align:center;font-family:"Montserrat",Arial,sans-serif;font-weight:400;font-size:33px;color:var(--white);text-transform:uppercase}
  .card{position:absolute;top:186px;width:265px;color:var(--white)}
  .card-photo{height:152px}
  .card h3{margin-top:28px;font-family:"Montserrat",Arial,sans-serif;font-weight:500;font-size:18px}
  .card p{margin-top:12px;font-size:10.8px;line-height:20px;color:var(--muted)}
  .btn{display:inline-block;border:2px solid currentColor;padding:9px 14px;font-family:"Montserrat",Arial,sans-serif;font-size:11px;font-weight:500;text-transform:uppercase}
  .card .btn{margin-top:18px;color:var(--white)}

  /* Connection video */
  .connect{top:1827px;height:556px}
  .connect .section-title{position:absolute;left:173px;top:84px;font-size:35px;line-height:38px;font-weight:500}
  .connect .copy{position:absolute;left:173px;top:176px;width:310px}
  .connect .btn{position:absolute;left:173px;top:398px;color:var(--ink)}
  .connect-shadow{position:absolute;left:493px;top:124px;width:533px;height:326px;background:var(--shadow-block)}
  .connect-video{position:absolute;left:502px;top:99px;width:524px;height:341px;
    background:radial-gradient(circle at 45% 45%,#5a5a5a,#1c1c1c 60%,#0c0c0c)}
  .player-bar{position:absolute;left:0;bottom:0;width:100%;height:26px;background:rgba(0,0,0,.55)}
  .player-progress{position:absolute;left:0;top:0;height:3px;width:100%;background:rgba(255,255,255,.3)}
  .player-progress span{display:block;width:40px;height:3px;background:var(--accent)}
  .player-time{position:absolute;left:64px;top:8px;font-size:9px;color:var(--white)}

  /* Footer */
  .site-footer{top:2383px;height:300px;color:var(--white)}
  .site-footer .brand{left:173px;top:58px;font-size:12px}
  .foot-col{position:absolute;top:65px}
  .foot-col h4{font-family:"Montserrat",Arial,sans-serif;font-weight:500;font-size:13px;letter-spacing:.04em}
  .foot-col ul{list-style:none;margin-top:12px;margin-left:5px}
  .foot-col li{font-size:10.5px;line-height:21px;color:var(--muted)}
  .signup{display:flex;margin-top:12px;width:290px;height:32px;border-radius:16px;overflow:hidden}
  .signup span{flex:1;background:#efefef;color:#999;font-size:10px;padding:9px 14px}
  .signup b{width:84px;background:#111;color:var(--white);font-family:"Montserrat",Arial,sans-serif;font-weight:500;font-size:11px;text-align:center;line-height:32px;text-transform:uppercase}
  .follow{display:flex;align-items:center;gap:6px;margin-top:18px;font-family:"Montserrat",Arial,sans-serif;font-size:13px}
  .follow span{margin-right:4px}
  .follow i{width:26px;height:26px;border:2px solid var(--white);border-radius:50%}
  .foot-rule{position:absolute;left:173px;top:242px;width:855px;height:1px;background:rgba(255,255,255,.35)}
  .legal{position:absolute;left:0;width:1200px;top:262px;text-align:center;font-size:11px;color:var(--muted)}
</style>
</head>
<body>

<header class="hero stone">
  <div class="brand"><i class="brand-dot"></i>Lumen Harbor Media</div>
  <nav class="main-nav">
    <span>Home</span><span>Rockstars</span><span>Local Legends</span><span>Unsung Heroes</span><span>The Band</span><span>The Partners</span><span>You &amp; Dorian Fleck</span>
  </nav>
  <div class="hero-video" role="img" aria-label="Conference crowd holding up cards towards a speaker on stage">
    <svg class="play" width="80" height="80" viewBox="0 0 80 80">
      <circle cx="40" cy="40" r="36" fill="rgba(0,0,0,.35)" stroke="#fff" stroke-width="3"/>
      <polygon points="32,25 58,40 32,55" fill="#fff"/>
    </svg>
  </div>
</header>

<section class="gigs">
  <div class="gigs-shadow"></div>
  <div class="gigs-photo" role="img" aria-label="Speaker with microphone facing an audience holding up phone lights"></div>
  <h2 class="section-title">The Gigs</h2>
  <p class="copy">Sed ut ploerspiciatis unde omnis isna tus error sit voluptat em accusantium doloremque laud antium, totam remlope riam, eaque ipsa quae ab illo inventore veritatis et quloas hiteclot obeatae vitae dicta sunt explicabo loremo enlr im ipsam voluptatem quia voluptas sit asprnaturut odit alout fugit, sed quia consequunt lour magni dolores eos qui rat ne voluptatem sequuntulohrr magni doloreolores eos qui ratio nev oluptatem sequuntur magsr magni dolores eos qui rationevoluptatem sequuntur magni doloreolores eos qui ratio nevoluptatemlor sequuntur mao nev oluptatem sequuntur magsr magni dolores eos qui rationevolup tat em sequuntur magni doloreol ores eos qui ratio nev lolu ptatem uuntur magni.</p>
</section>

<section class="features stone">
  <h2>Rock Stars, Local Legends &amp; Unsung Heroes</h2>
  <article class="card" style="left:173px">
    <div class="card-photo" role="img" aria-label="Speaker on a stage lit in blue" style="background:linear-gradient(120deg,#1b2a6a,#3a3f8a 45%,#c9a08a 75%,#2a2a3a)"></div>
    <h3>Neue oloremisro uisuam</h3>
    <p>Sed ut perspiciatis unde omnis iste natus er ror sit voluptatem accusantium doloremque laudantium, totam rem aperiam.</p>
    <span class="btn">Read More</span>
  </article>
  <article class="card" style="left:467px">
    <div class="card-photo" role="img" aria-label="Business leaders at a long roundtable luncheon" style="background:linear-gradient(120deg,#3a2418,#7a5a40 50%,#d8cfc0 70%,#3a2a20)"></div>
    <h3>Neue oloremisro uisuam</h3>
    <p>Sed ut perspiciatis unde omnis iste natus er ror sit voluptatem accusantium doloremque laudantium, totam rem aperiam.</p>
    <span class="btn">Read More</span>
  </article>
  <article class="card" style="left:762px">
    <div class="card-photo" role="img" aria-label="Attendees seated in a conference audience" style="background:linear-gradient(120deg,#6a2a18,#b0603a 45%,#e8e0d8 80%,#8a8a8a)"></div>
    <h3>Neue oloremisro uisuam</h3>
    <p>Sed ut perspiciatis unde omnis iste natus er ror sit voluptatem accusantium doloremque laudantium, totam rem aperiam.</p>
    <span class="btn">Read More</span>
  </article>
</section>

<section class="connect">
  <h2 class="section-title">You &amp;<br>Dorian Fleck</h2>
  <p class="copy">Sed ut ploerspiciatis unde omnis isna tus error sit voluptat em accusantium doloremque laud antium, totam remlope riam, eaque ipsa quae ab illo inventore veritatis et quloas hiteclot obeatae vitae dicta sunt explicabo loremo enlr im ipsam voluptatem quia voluptas sit asprnaturut odit alout fugit, sed quia consequunt lour magni dolores eos qui rat ne voluptatem sequuntulohrr magni doloreolores eos qui ratio nev oluptatem sequuntur magsr magni dolores eos qui rationevoluptatem sequuntur mao</p>
  <span class="btn">Read More</span>
  <div class="connect-shadow"></div>
  <div class="connect-video" role="img" aria-label="Video still of Dorian Fleck in black and white">
    <div class="player-bar">
      <div class="player-progress"><span></span></div>
      <svg width="60" height="26" viewBox="0 0 60 26" style="position:absolute;left:8px;top:0">
        <rect x="2" y="9" width="3" height="10" fill="#fff"/><rect x="8" y="9" width="3" height="10" fill="#fff"/>
        <polygon points="22,9 29,14 22,19" fill="#fff"/><rect x="29" y="9" width="2" height="10" fill="#fff"/>
        <polygon points="40,12 43,12 47,9 47,19 43,16 40,16" fill="#fff"/>
      </svg>
      <span class="player-time">0:13 / 2:59</span>
      <svg width="90" height="26" viewBox="0 0 90 26" style="position:absolute;right:6px;top:0">
        <rect x="4" y="9" width="12" height="9" fill="none" stroke="#fff" stroke-width="1.5"/>
        <circle cx="32" cy="13.5" r="4" fill="none" stroke="#fff" stroke-width="2"/>
        <rect x="48" y="9" width="13" height="9" fill="none" stroke="#fff" stroke-width="1.5"/>
        <rect x="70" y="9" width="14" height="9" fill="none" stroke="#fff" stroke-width="1.5"/>
      </svg>
    </div>
  </div>
</section>

<footer class="site-footer stone">
  <div class="brand"><i class="brand-dot"></i>Lumen Harbor Media</div>
  <div class="foot-col" style="left:413px">
    <h4>Company</h4>
    <ul><li>Sed ut perspiciatis</li><li>Unde omnis iste</li><li>Voluptatem</li><li>Accusantium</li><li>Doloremqu</li></ul>
  </div>
  <div class="foot-col" style="left:581px">
    <h4>Links</h4>
    <ul><li>Sed ut perspiciatis</li><li>Unde omnis iste</li><li>Voluptatem</li><li>Accusantium</li><li>Dolorem</li></ul>
  </div>
  <div class="foot-col" style="left:738px">
    <h4>Newsletter</h4>
    <div class="signup"><span>Email:</span><b>Sign Up</b></div>
    <div class="follow"><span>Follow us on</span><i></i><i></i></div>
  </div>
  <div class="foot-rule"></div>
  <p class="legal">© 2019 All Rights Are Reserved Terms of Use | Privacy Policy</p>
</footer>

</body>
</html>
```